Stationery Design Project

We need letterhead and business cards designed for our consulting firm. Color scheme, mostly deep blue (see logo). We are a commercial consulting work out firm, nationwide (large loans, $10MM and up). Visit our website for more info.
Updates

Project Deadline Extended
Reason: Meeting tomorrow morning to make final final decision. Would like this project to stay open to be able to provide feed back and receive final edits and approve. Thank you!!!

Target Market(s)

High end investors

Industry/Entity Type

Business

Requirements
Must have
• Letterhead must have the logo and the address

4817 Larkmoor Avenue, Suite 210, San Diego, CA 92107
Nice to have
• It would be nice to incorporate a watermark of all or some portion of the logo on the letterhead, or at least for the 2nd sheets.

Maybe our phone number: 858.555.0174
and/or webiste: www.tollandridgecap.example
Should not have
• Target users and audience of this will be men so, frilly or whimsical type designs are not preferred.

```html
<!DOCTYPE html>
<html lang="en">
<head>
<meta charset="utf-8">
<title>Tolland Ridge Capital – Business Card Options</title>
<link rel="stylesheet" href="https://fonts.googleapis.com/css2?family=PT+Sans:wght@400&display=swap">
<style>
  :root {
    --backdrop: #dcd5dc;
    --card: #ffffff;
    --navy: #25297a;
    --stone: #c4c1bc;
    --ink: #545454;
    --muted: #8c8c8c;
    --rule: #4a4a4a;
    --on-navy: #ffffff;
  }
  * { margin: 0; padding: 0; box-sizing: border-box; }
  html, body {
    width: 867px; height: 1200px; overflow: hidden;
    background: var(--backdrop);
    font-family: "PT Sans", Arial, sans-serif;
  }
  .sheet { position: relative; width: 867px; height: 1200px; }
  .card {
    position: absolute; width: 358px; height: 220px;
    background: var(--card); overflow: hidden;
  }
  .card--one { left: 217px; top: 36px; }
  .card--two { left: 217px; top: 368px; }
  .card--three { left: 219px; top: 712px; }

  .brand {
    position: absolute; left: 0; top: 14px; width: 132px; height: 61px;
    display: flex; align-items: center; justify-content: center;
    background: var(--stone);
  }
  .card--two .brand, .card--three .brand { background: var(--navy); }
  .brand__name {
    font-size: 13px; letter-spacing: 0.5px; color: var(--ink);
    text-transform: uppercase; text-align: center; line-height: 1.1;
  }
  .card--two .brand__name, .card--three .brand__name { color: #b9bccc; }

  .holder {
    position: absolute; left: 0; right: 0; top: 95px; text-align: center;
    color: var(--ink); padding-left: 12px;
  }
  .holder__name { font-size: 17px; line-height: 20px; }
  .holder__title { font-size: 10px; line-height: 14px; margin-top: 3px; }

  .rule {
    position: absolute; left: 0; right: 0; top: 175px; height: 3px;
    background: var(--rule);
  }
  .contact {
    position: absolute; left: 0; right: 0; top: 178px; bottom: 0;
    text-align: center; color: var(--muted); padding-top: 1px;
    white-space: nowrap;
  }
  .card--three .contact { background: var(--navy); color: var(--on-navy); }
  .contact__line { font-size: 8.5px; line-height: 11px; }
  .contact__fine { font-size: 5px; line-height: 7.5px; }
</style>
</head>
<body>
<main class="sheet">

  <section class="card card--one">
    <div class="brand"><span class="brand__name">Tolland Ridge<br>Capital</span></div>
    <div class="holder">
      <p class="holder__name">DALE WHITCOMBE</p>
      <p class="holder__title">CHIEF EXECUTIVE OFFICER</p>
    </div>
    <div class="rule"></div>
    <div class="contact">
      <p class="contact__line">4817 Larkmoor Avenue, Suite 210, San Diego, CA 92107</p>
      <p class="contact__line">Phone 858.555.0174 Cel. 858.555.0188</p>
      <p class="contact__fine">E-MAIL : info@tollandridgecap.example</p>
      <p class="contact__fine">WWW : www.tollandridgecap.example</p>
    </div>
  </section>

  <section class="card card--two">
    <div class="brand"><span class="brand__name">Tolland Ridge<br>Capital</span></div>
    <div class="holder">
      <p class="holder__name">DALE WHITCOMBE</p>
      <p class="holder__title">CHIEF EXECUTIVE OFFICER</p>
    </div>
    <div class="rule"></div>
    <div class="contact">
      <p class="contact__line">4817 Larkmoor Avenue, Suite 210, San Diego, CA 92107</p>
      <p class="contact__line">Phone 858.555.0174 Cel. 858.555.0188</p>
      <p class="contact__fine">E-MAIL : info@tollandridgecap.example</p>
      <p class="contact__fine">WWW : www.tollandridgecap.example</p>
    </div>
  </section>

  <section class="card card--three">
    <div class="brand"><span class="brand__name">Tolland Ridge<br>Capital</span></div>
    <div class="holder">
      <p class="holder__name">DALE WHITCOMBE</p>
      <p class="holder__title">CHIEF EXECUTIVE OFFICER</p>
    </div>
    <div class="rule"></div>
    <div class="contact">
      <p class="contact__line">4817 Larkmoor Avenue, Suite 210, San Diego, CA 92107</p>
      <p class="contact__line">Phone 858.555.0174 Cel. 858.555.0188</p>
      <p class="contact__fine">E-MAIL : info@tollandridgecap.example</p>
      <p class="contact__fine">WWW : www.tollandridgecap.example</p>
    </div>
  </section>

</main>
</body>
</html>
```